Brightpath Orthodontics business card design

Need a business card design that reflects our re-branding (orthodontic office - braces) and a new partnership with a pediatric dental office. We would like to include "for adults and children" on the card as well so adults know they are welcome to get their braces here as well. Office design is modern and would like business card to reflect a modern type look. Here's the text we would like to be included on the card:

Darren Holloway, DDS, MSD
5214 West Maple Avenue, Suite 204
Mansfield, TX 76099
817-555-0143
www.brightpathortho.example
info@brightpathortho.example
Updates

Can we add the following to the existing designs? Darren Holloway, DDS, MSD 5214 West Maple Avenue, Suite 204 Mansfield, TX 76099 817-555-0143

Does anyone have any more vertical designs available? Thanks!

Industry/Entity Type

Dental

```html
<!DOCTYPE html>
<html lang="en">
<head>
<meta charset="utf-8">
<title>Brightpath Orthodontics – Business Card</title>
<link rel="stylesheet" href="https://fonts.googleapis.com/css2?family=Open+Sans:wght@400;600;700;800&display=swap">
<style>
  :root {
    --bg: #e9e6e1;
    --card-light: #f7b928;
    --card-dark: #ee9a17;
    --magenta: #ec1fbf;
    --magenta-edge: #c9169f;
    --ink: #232323;
    --name-blue: #2aa7df;
    --white: #ffffff;
    --tooth-light: #ffffff;
    --tooth-shade: #d9d9d9;
    --tooth-edge: #2b2b2b;
  }
  * { box-sizing: border-box; margin: 0; padding: 0; }
  html, body {
    width: 1200px; height: 1023px; overflow: hidden;
    background: var(--bg);
    font-family: "Open Sans", Arial, sans-serif;
  }
  .canvas {
    position: relative; width: 1200px; height: 1023px;
    display: flex; align-items: center; justify-content: center;
  }
  .card {
    position: relative; width: 1050px; height: 600px;
    border-radius: 6px; overflow: hidden;
    background: linear-gradient(160deg, var(--card-light) 0%, var(--card-dark) 100%);
    box-shadow: 0 14px 40px rgba(0,0,0,.18);
  }
  .tooth-art {
    position: absolute; left: 40px; top: 262px;
    width: 370px; height: 380px;
    border-radius: 90px 90px 0 0;
    border: 6px solid var(--tooth-edge);
    background: radial-gradient(ellipse at 45% 35%, var(--tooth-light) 0%, var(--tooth-light) 45%, var(--tooth-shade) 100%);
  }
  .brand {
    position: absolute; left: 64px; top: 52px;
    display: flex; align-items: center; gap: 18px;
  }
  .brand-dot {
    width: 54px; height: 54px; border-radius: 50%;
    background: var(--white);
  }
  .brand-name {
    font-weight: 800; font-size: 46px; color: var(--ink);
    letter-spacing: .2px; line-height: 1;
  }
  .tagline {
    position: absolute; left: 138px; top: 116px;
    font-size: 20px; font-weight: 600; color: var(--ink);
    letter-spacing: .3px;
  }
  .doctor {
    position: absolute; left: 66px; top: 160px;
    font-size: 27px; font-weight: 600; color: var(--ink);
    letter-spacing: .4px;
  }
  .doctor-name { color: var(--name-blue); font-weight: 700; text-transform: uppercase; }
  .contact-band {
    position: absolute; left: 420px; right: 0; top: 216px; height: 186px;
    background: var(--magenta);
    border-radius: 93px 0 0 93px;
    border: 4px solid var(--magenta-edge); border-right: none;
    padding: 26px 40px 0 0;
    display: flex; flex-direction: column; align-items: flex-end; gap: 10px;
  }
  .contact-line {
    display: flex; align-items: center; gap: 18px;
    color: var(--white); font-size: 27px; font-weight: 400;
  }
  .contact-icon { width: 34px; height: 34px; flex: none; }
  .address {
    position: absolute; right: 40px; top: 428px; text-align: right;
    color: var(--ink); font-weight: 700; font-size: 23px;
    text-transform: uppercase; line-height: 1.45; letter-spacing: .3px;
  }
</style>
</head>
<body>
<main class="canvas">
  <section class="card" aria-label="Brightpath Orthodontics business card">
    <div class="tooth-art" role="img" aria-label="Large white cartoon tooth illustration with dark outline"></div>

    <div class="brand">
      <span class="brand-dot"></span>
      <span class="brand-name">Brightpath Orthodontics</span>
    </div>
    <p class="tagline">for adults and children</p>

    <p class="doctor"><span class="doctor-name">Darren Holloway</span>, DDS, MSD</p>

    <div class="contact-band">
      <p class="contact-line">817-555-0143
        <svg class="contact-icon" viewBox="0 0 34 34" aria-hidden="true">
          <circle cx="17" cy="17" r="15" fill="none" stroke="#fff" stroke-width="2.5"/>
          <path d="M11 10c1-1 2.5-1 3 0l1.6 3c.4.8 0 1.5-.6 2l-1 .8c.8 1.8 2.2 3.2 4 4l.8-1c.5-.6 1.2-1 2-.6l3 1.6c1 .5 1 2 0 3-2 2-5 2-8.5-1.2S8.7 12.3 11 10z" fill="#fff"/>
        </svg>
      </p>
      <p class="contact-line">info@brightpathortho.example
        <svg class="contact-icon" viewBox="0 0 34 34" aria-hidden="true">
          <circle cx="17" cy="17" r="15" fill="none" stroke="#fff" stroke-width="2.5"/>
          <rect x="9" y="11.5" width="16" height="11" rx="1.5" fill="none" stroke="#fff" stroke-width="2"/>
          <path d="M9.5 12.5l7.5 6 7.5-6" fill="none" stroke="#fff" stroke-width="2"/>
        </svg>
      </p>
      <p class="contact-line">www.brightpathortho.example
        <svg class="contact-icon" viewBox="0 0 34 34" aria-hidden="true">
          <circle cx="17" cy="17" r="15" fill="none" stroke="#fff" stroke-width="2.5"/>
          <circle cx="17" cy="17" r="8.5" fill="none" stroke="#fff" stroke-width="1.8"/>
          <ellipse cx="17" cy="17" rx="3.8" ry="8.5" fill="none" stroke="#fff" stroke-width="1.6"/>
          <path d="M8.5 17h17M10 13h14M10 21h14" stroke="#fff" stroke-width="1.4"/>
        </svg>
      </p>
    </div>

    <p class="address">5214 West Maple Avenue, Suite 204<br>Mansfield, TX 76099</p>
  </section>
</main>
</body>
</html>
```